Nutrient Guild of Meridia Website Creation

Nutrient Guild of Meridia seeks a membership website that is visually dynamic, suitable for all who seek knowledge and inspiration about maximizing their health and wellbeing. see nutrientguildofmeridia.com

Target Market(s)

Scientists, Media, Medical Professionals, Nutritionists, Public

Industry/Entity Type

Nutrition

Number of Pages Required

5+ page

Font styles to use
Sans Serif

Colors
0355a3
ec1f27

Requirements
Must have
• Large Pictures, full screen
• Areas for video, blog, articles
• Membership sign in/ Public Access
• Easy to Edit/Add Content
• Merchant Ready
• please check out http://greenleafcircle.org This is what I want it to resemble.
Nice to have
• Red White and Blue but not static, old fashioned, but upbeat.
• Movement - subtle
Should not have
• Should not look Governmental-ish
• Flat look
• Small page
• should not look like the basic site at www.nutrientguildofmeridia.com

```html
<!DOCTYPE html>
<html lang="en">
<head>
<meta charset="utf-8">
<title>Nutrient Guild of Meridia</title>
<link href="https://fonts.googleapis.com/css2?family=Lato:wght@400;700;900&display=swap" rel="stylesheet">
<style>
:root{
  --blue:#0355a3;
  --navy:#0d1a4a;
  --red:#ec1f27;
  --white:#ffffff;
  --ink:#333a45;
  --grey:#6b717a;
}
*{box-sizing:border-box;margin:0;padding:0}
html,body{width:1200px;height:2880px;overflow:hidden}
body{font-family:"Lato",sans-serif;color:var(--ink);background:var(--white);position:relative}

/* header */
.site-header{position:absolute;top:0;left:0;width:1200px;height:132px;background:var(--white);z-index:3;box-shadow:0 2px 8px rgba(0,0,0,.15)}
.brand{position:absolute;left:110px;top:10px;display:flex;align-items:center;gap:12px}
.brand-mark{width:112px;height:112px;border-radius:50%;background:var(--navy)}
.brand-name{font-weight:900;font-size:17px;color:var(--navy);width:150px;line-height:1.2;text-transform:uppercase}
.topbar{position:absolute;right:110px;top:8px;display:flex;gap:12px;font-size:14px;align-items:center;white-space:nowrap}
.topbar .phone{color:var(--grey)}
.topbar .tb-btn{background:var(--red);color:var(--white);padding:3px 9px;font-weight:700;font-size:12px}
.topbar .tb-btn.dark{background:var(--navy)}
.main-nav{position:absolute;left:408px;top:0;height:132px;display:flex;align-items:flex-end;gap:22px;padding-bottom:46px;white-space:nowrap}
.main-nav a{color:var(--navy);font-size:18px;font-weight:700;text-decoration:none;text-transform:uppercase}
.main-nav a.active{background:var(--red);color:var(--white);height:132px;width:80px;text-align:center;padding-top:66px;margin-bottom:-46px}
.main-nav .sep{color:#bbb;font-size:18px}

/* hero */
.hero{position:absolute;top:0;left:0;width:1200px;height:672px;background:radial-gradient(ellipse at 40% 55%,#e23b1f 0,#dc6a2c 22%,#e0a93a 34%,#8dae3a 48%,#4f7a28 66%,#eeeee6 86%)}
.hero-arrow{position:absolute;top:364px;width:36px;height:36px;border-radius:50%;background:rgba(255,255,255,.85);color:var(--navy);font-size:22px;text-align:center;line-height:34px;font-weight:900}
.join-badge{position:absolute;left:770px;top:280px;width:220px;height:220px;border-radius:50%;background:var(--white);border:6px solid #dcdcdc;text-align:center;padding-top:54px}
.join-badge p{font-weight:900;font-size:18px;color:var(--navy);line-height:1.2;text-transform:uppercase}
.join-badge span{display:inline-block;margin-top:10px;background:var(--red);color:var(--white);font-weight:900;font-size:14px;padding:5px 14px}

/* founding */
.founding{position:absolute;top:672px;left:0;width:1200px;height:308px;background:var(--navy);text-align:center;color:var(--white)}
.founding h2{font-weight:400;font-size:42px;margin-top:40px}
.founding p{width:1000px;margin:24px auto 0;font-size:16px;line-height:1.55;font-weight:700}
.btn-red{display:inline-block;background:var(--red);color:var(--white);font-weight:900;font-size:20px;padding:9px 26px;margin-top:22px;border:2px solid var(--white)}

/* video */
.video{position:absolute;top:980px;left:0;width:1200px;height:548px;background:linear-gradient(180deg,rgba(255,255,255,.84),rgba(255,255,255,.7)),linear-gradient(90deg,#d9a24a,#a9c26a 50%,#e07a52);text-align:center}
.section-title{font-weight:900;font-size:50px;color:var(--navy)}
.section-title em{font-style:normal;color:var(--red)}
.video .section-title{margin-top:22px}
.title-rule{width:500px;height:2px;background:#999;margin:12px auto 0;position:relative}
.title-rule i{position:absolute;left:240px;top:-10px;width:20px;height:20px;border-radius:50%;background:var(--navy);border:3px solid #fff}
.video-area{position:absolute;left:330px;top:140px;width:540px;height:408px;background:linear-gradient(135deg,#cfd0d2,#6b6e73)}

/* features */
.features{position:absolute;top:1528px;left:0;width:1200px;height:332px;display:flex}
.feature{width:600px;height:332px;color:var(--white);text-align:center;padding-top:44px}
.feature.research{background:var(--navy)}
.feature.products{background:var(--red)}
.feature h3{font-weight:900;font-size:32px;margin-top:10px;text-transform:uppercase}
.feature p{width:420px;margin:12px auto 0;font-size:15px;line-height:1.45}

/* articles */
.articles{position:absolute;top:1860px;left:0;width:1200px;height:452px;background:var(--white);text-align:center}
.articles .section-title{margin-top:30px}
.cards{position:absolute;left:125px;top:150px;display:flex;gap:40px}
.card{width:290px;text-align:left}
.card-photo{height:160px;background:linear-gradient(135deg,#c8d3dd,#5b6b7c)}
.card .date{font-size:13px;color:var(--ink);margin-top:12px}
.card p{font-size:13px;line-height:1.4;margin-top:8px;color:var(--grey)}
.art-arrow{position:absolute;top:210px;font-size:34px;color:var(--navy);font-weight:900}

/* footer nav */
.footer-nav{position:absolute;top:2312px;left:0;width:1200px;height:76px;background:var(--navy)}
.footer-nav a{position:absolute;top:26px;color:var(--white);font-size:18px;font-weight:700;text-decoration:none;text-transform:uppercase;white-space:nowrap}
.footer-mark{position:absolute;left:570px;top:-30px;width:60px;height:60px;border-radius:50%;background:var(--navy);border:4px solid var(--white)}

/* contact */
.contact{position:absolute;top:2388px;left:0;width:1200px;height:240px;background:linear-gradient(135deg,#4b4f56,#6f7379);color:var(--white);text-align:center}
.contact h2{font-size:34px;font-weight:400;margin-top:26px;text-transform:uppercase}
.contact .thanks{font-size:22px;margin-top:22px}
.contact-row{position:absolute;left:180px;top:150px;display:flex;gap:70px;text-align:left;font-size:16px;line-height:1.4}
.contact-item{display:flex;align-items:center;gap:14px}
.contact-item .ico{width:48px;height:48px;border-radius:50%;background:rgba(255,255,255,.25);display:flex;align-items:center;justify-content:center}

/* form */
.form-band{position:absolute;top:2628px;left:0;width:1200px;height:224px;background:var(--red);color:var(--white)}
.form-band h3{text-align:center;font-weight:400;font-size:26px;margin-top:18px}
.field{position:absolute;background:var(--white);color:#888;font-size:14px;padding:6px 10px;height:30px}
.send{position:absolute;left:760px;top:150px;width:120px;height:34px;background:var(--navy);color:var(--white);font-weight:900;font-size:17px;text-align:center;line-height:34px}
.copyright{position:absolute;top:2852px;left:0;width:1200px;height:28px;background:var(--navy);color:#cfd3de;font-size:12px;text-align:center;line-height:28px}
</style>
</head>
<body>

<section class="hero" role="img" aria-label="Large photo of fresh vegetables and fruit: tomatoes, peppers, broccoli, cucumbers and apples"></section>
<div class="hero-arrow" style="left:90px">&#8249;</div>
<div class="hero-arrow" style="left:1074px">&#8250;</div>
<div class="join-badge"><p>Join the<br>Nutrient Guild<br>of Meridia Today</p><span>REGISTER NOW</span></div>

<header class="site-header">
  <div class="brand"><div class="brand-mark"></div><div class="brand-name">Nutrient Guild of Meridia</div></div>
  <div class="topbar"><span class="phone">&#9742; (555) 014-2290</span><span class="tb-btn">LOGIN</span><span class="tb-btn dark">REGISTER</span></div>
  <nav class="main-nav">
    <a class="active" href="#">Home</a>
    <a href="#">About Us</a><span class="sep">|</span>
    <a href="#">Membership Opportunities</a><span class="sep">|</span>
    <a href="#">Contact Us</a>
  </nav>
</header>

<section class="founding">
  <h2>Seeking Founding Members</h2>
  <p>We Are Searching For Those Who Would Relish The Opportunity To Shape The Direction Of The Society As We Become The Ultimate, Evidence-based, Central Resource For Scientists, Providers, Entrepreneurs, Patients, And All Interested Parties. I Am Accepting Nominations For The 13 Founder's That Will Become The Leaders Of The Think Tank - Those Accomplished And Ready To Multiply Their Efforts Through Innovation, Education, And Motivation.</p>
  <span class="btn-red">JOIN US TODAY</span>
</section>

<section class="video">
  <h2 class="section-title">Our <em>Video</em></h2>
  <div class="title-rule"><i></i></div>
  <div class="video-area" role="img" aria-label="Photo of hands holding a tablet that plays the introductory video"></div>
</section>

<section class="features">
  <div class="feature research">
    <svg width="56" height="56" viewBox="0 0 60 60" fill="none" stroke="#fff" stroke-width="4"><path d="M22 6h16M26 6v18L12 50a4 4 0 0 0 4 6h28a4 4 0 0 0 4-6L34 24V6"/><path d="M18 40h24"/></svg>
    <h3>Research</h3>
    <p>Lorem ipsum dolor sit amet, consectetur adipiscing elit, sed do eiusmod tempor incididunt ut labore et dolore magna aliqua ut enim ad minim veniam quis nostrud.</p>
  </div>
  <div class="feature products">
    <svg width="56" height="56" viewBox="0 0 60 60" fill="none" stroke="#fff" stroke-width="4" stroke-linecap="round"><path d="M10 50L36 24M40 8a10 10 0 0 0-4 16l8 8a10 10 0 0 0 16-4l-6 2-6-6 2-6z"/><path d="M50 50L28 28M8 8l10 10"/></svg>
    <h3>Products &amp; Services</h3>
    <p>Lorem ipsum dolor sit amet, consectetur adipiscing elit, sed do eiusmod tempor incididunt ut labore et dolore magna aliqua ut enim ad minim veniam quis nostrud.</p>
  </div>
</section>

<section class="articles">
  <h2 class="section-title">Featured <em>Articles</em></h2>
  <div class="title-rule"><i></i></div>
  <span class="art-arrow" style="left:70px">&#8249;</span>
  <span class="art-arrow" style="left:1110px">&#8250;</span>
  <div class="cards">
    <div class="card"><div class="card-photo" role="img" aria-label="Group of professionals in silhouette against a bright window"></div><div class="date">28 Oct 2015</div><p>Lorem ipsum dolor sit amet, consectetur adipiscing elit, sed do eiusmod tempor incididunt labore et dolore magna.</p></div>
    <div class="card"><div class="card-photo" role="img" aria-label="Hand holding a tablet showing a world map"></div><div class="date">28 Oct 2015</div><p>Lorem ipsum dolor sit amet, consectetur adipiscing elit, sed do eiusmod tempor incididunt labore et dolore magna.</p></div>
    <div class="card"><div class="card-photo" role="img" aria-label="Team of business people in suits"></div><div class="date">28 Oct 2015</div><p>Lorem ipsum dolor sit amet, consectetur adipiscing elit, sed do eiusmod tempor incididunt labore et dolore magna.</p></div>
  </div>
</section>

<nav class="footer-nav">
  <div class="footer-mark"></div>
  <a href="#" style="left:300px">Home</a>
  <a href="#" style="left:440px">About Us</a>
  <a href="#" style="left:650px">Membership Opportunities</a>
  <a href="#" style="left:950px">Contact Us</a>
</nav>

<section class="contact" role="img" aria-label="Muted street map background">
  <h2>Let's Get Started</h2>
  <p class="thanks">Thank you for your interest in contacting Nutrient Guild of Meridia</p>
  <div class="contact-row">
    <div class="contact-item"><span class="ico"><svg width="22" height="28" viewBox="0 0 22 28"><path d="M11 0a11 11 0 0 0-11 11c0 8 11 17 11 17s11-9 11-17A11 11 0 0 0 11 0z" fill="#fff"/><circle cx="11" cy="11" r="4" fill="#5d6168"/></svg></span><span>4665 Orchard Lane<br>Meridia City, MR 70127</span></div>
    <div class="contact-item"><span class="ico"><svg width="24" height="24" viewBox="0 0 24 24"><path d="M5 2l4 1 2 5-3 2a13 13 0 0 0 6 6l2-3 5 2 1 4c-1 2-3 3-5 3C9 22 2 15 2 7c0-2 1-4 3-5z" fill="#fff"/></svg></span><span>555-014-7731</span></div>
    <div class="contact-item"><span class="ico"><svg width="26" height="20" viewBox="0 0 26 20" fill="none" stroke="#fff" stroke-width="2.5"><rect x="1" y="1" width="24" height="18"/><path d="M1 1l12 10L25 1"/></svg></span><span>hello@nutrientguildofmeridia.com</span></div>
  </div>
</section>

<section class="form-band">
  <h3>Please Fill Out The Form Below</h3>
  <div class="field" style="left:140px;top:66px;width:300px">Your Name</div>
  <div class="field" style="left:450px;top:66px;width:300px">Email</div>
  <div class="field" style="left:760px;top:66px;width:300px">Phone</div>
  <div class="field" style="left:140px;top:106px;width:600px;height:96px">Comments</div>
  <div class="send">SEND</div>
</section>

<footer class="copyright">Copyright &copy; 2015 Nutrient Guild of Meridia. All Rights Reserved.</footer>

</body>
</html>
```